Business Image

I have recently had a new company logo made up and require some new business cards to go with it.

Target Market(s)

Developers & high worth clients.

Industry/Entity Type

Business

Contact Information for Business Card

The business is in the construction/management industry. It needs to be classy but have a industrial feel. I would like the business card to be a elegant presentation in itself.

Requirements
Must have
• Current logo & company name. Colouring needs to be the same as the current design also.
Nice to have
• A few different designs & presentations of single and double sided business cards.

```html
<!DOCTYPE html>
<html lang="en">
<head>
<meta charset="utf-8">
<title>Halvern Build Group – Business Card</title>
<link href="https://fonts.googleapis.com/css2?family=Libre+Baskerville:wght@700&family=Open+Sans:wght@400;600&display=swap" rel="stylesheet">
<style>
  :root {
    --page: #e9e7e3;
    --card: #f7f7f5;
    --steel-blue: #6691c6;
    --steel-blue-dark: #4f77aa;
    --charcoal: #3b3c3e;
    --ink: #262626;
    --tab-grey: #c3c5c8;
    --white: #ffffff;
  }
  * { box-sizing: border-box; margin: 0; padding: 0; }
  html, body { width: 1200px; height: 1000px; overflow: hidden; }
  body {
    background: var(--page);
    display: flex;
    flex-direction: column;
    align-items: center;
    justify-content: center;
    gap: 56px;
    font-family: "Open Sans", Arial, sans-serif;
  }
  .card {
    position: relative;
    width: 700px;
    height: 400px;
    background: var(--card);
    box-shadow: 0 6px 18px rgba(0,0,0,0.18);
    overflow: hidden;
  }

  /* Brand lockup */
  .brand {
    display: flex;
    align-items: center;
    gap: 16px;
  }
  .brand-mark {
    width: 30px;
    height: 30px;
    background: var(--steel-blue);
    flex: none;
  }
  .brand-name {
    font-family: "Libre Baskerville", Georgia, serif;
    font-weight: 700;
    color: var(--steel-blue);
    line-height: 1.05;
    text-transform: uppercase;
  }

  /* Front */
  .card-front .brand {
    position: absolute;
    top: 92px;
    left: 0;
    right: 0;
    justify-content: center;
  }
  .card-front .brand-name { font-size: 40px; letter-spacing: 1px; }
  .card-front .rule {
    position: absolute;
    left: 0; right: 0;
    top: 262px;
    height: 14px;
    background: var(--charcoal);
  }
  .card-front .band {
    position: absolute;
    left: 0; right: 0;
    top: 276px;
    bottom: 0;
    background: var(--steel-blue);
  }

  /* Back */
  .card-back .brand {
    position: absolute;
    left: 34px;
    top: 150px;
    width: 220px;
    flex-direction: column;
    align-items: flex-start;
    gap: 12px;
  }
  .card-back .brand-name { font-size: 25px; }
  .contact-list {
    position: absolute;
    top: 14px;
    left: 270px;
    right: 0;
    list-style: none;
  }
  .contact-list .divider {
    height: 36px;
    margin-left: 44px;
    margin-right: 22px;
    background: var(--charcoal);
  }
  .contact-list .divider:first-child { height: 28px; }
  .contact-item {
    position: relative;
    height: 58px;
    background: var(--steel-blue);
    margin-right: 10px;
    display: flex;
    align-items: center;
    gap: 16px;
    padding-left: 40px;
    color: var(--white);
    font-size: 15px;
    box-shadow: 0 4px 6px rgba(0,0,0,0.25);
  }
  .contact-item::before {
    content: "";
    position: absolute;
    left: -12px;
    top: 0;
    width: 12px;
    height: 100%;
    background: var(--tab-grey);
  }
  .contact-icon {
    width: 26px;
    height: 26px;
    border-radius: 50%;
    background: var(--white);
    display: flex;
    align-items: center;
    justify-content: center;
    flex: none;
  }
  .contact-icon svg { width: 14px; height: 14px; fill: var(--steel-blue-dark); }
</style>
</head>
<body>

  <section class="card card-front" aria-label="Business card front">
    <div class="brand">
      <span class="brand-mark"></span>
      <span class="brand-name">Halvern Build Group</span>
    </div>
    <div class="rule"></div>
    <div class="band"></div>
  </section>

  <section class="card card-back" aria-label="Business card back">
    <div class="brand">
      <span class="brand-mark"></span>
      <span class="brand-name">Halvern<br>Build Group</span>
    </div>

    <ul class="contact-list">
      <li class="divider"></li>
      <li class="contact-item">
        <span class="contact-icon">
          <svg viewBox="0 0 16 16" aria-hidden="true"><path d="M5 1h6a1 1 0 0 1 1 1v12a1 1 0 0 1-1 1H5a1 1 0 0 1-1-1V2a1 1 0 0 1 1-1zm0 2v9h6V3H5zm3 10a.8.8 0 1 0 0 1.6.8.8 0 0 0 0-1.6z"/></svg>
        </span>
        <span class="contact-text">1 (555) 014-2280</span>
      </li>
      <li class="divider"></li>
      <li class="contact-item">
        <span class="contact-icon">
          <svg viewBox="0 0 16 16" aria-hidden="true"><path d="M3.6 1.5l2.1 2.6-1.3 1.6c.9 2 2.4 3.5 4.4 4.4l1.6-1.3 2.6 2.1-1.2 2.4C6.8 13.1 2.9 9.2 1.2 3.8z"/></svg>
        </span>
        <span class="contact-text">1 (555) 014-2291</span>
      </li>
      <li class="divider"></li>
      <li class="contact-item">
        <span class="contact-icon">
          <svg viewBox="0 0 16 16" aria-hidden="true"><path d="M8 1a5 5 0 0 1 5 5c0 3.5-5 9-5 9S3 9.5 3 6a5 5 0 0 1 5-5zm0 3a2 2 0 1 0 0 4 2 2 0 0 0 0-4z"/></svg>
        </span>
        <span class="contact-text">48 Foundry Lane, Millbrook, ST 20417, USA</span>
      </li>
      <li class="divider"></li>
      <li class="contact-item">
        <span class="contact-icon">
          <svg viewBox="0 0 16 16" aria-hidden="true"><path d="M1.5 3.5h13v9h-13zm1.3 1.2v.3L8 8.6l5.2-3.6v-.3zm0 1.8v4.8h10.4V6.5L8 10.1z"/></svg>
        </span>
        <span class="contact-text">d.marlow@halvernbuild.com</span>
      </li>
    </ul>
  </section>

</body>
</html>
```